Food Ingredient Manufacturer needs a Vector Design

BUSINESS OVERVIEW: particle processing of food ingredients. 1) we microencapsulate (apply a coating) to particles for a few different reasons (examples: taste/color masking, controlled or timed release of ingredient, nutrient stability, extending shelve-life, among others). 2) we agglomerate particles (make particles stick together to make them go into solution better/faster) Everything we do is customize to our customers specifications. We use the term "Solutions Engineering" quite a bit in our marketing materials.

COMPANY NAME: Harbor Milling Industries, trade name for our microencapsulation is "Quill Capsule" (both logos attached)

PROJECT OVERVIEW: I am looking for a vector graphic that can be used for a few different projects 1) trade magazine print ads 2) trade show banner & 10 x 10 booth 3) a quasi-logo that explains our primary business functions.

OTHER: logo uses the following blue color: RGB [0,191,231]; CMYK [71,0,0,0]; HEX [#00bfe7]. I would like to incorporate Navy Blue into more of our branding.

Target Market(s)

Business-to-business, R&D and Scientists

Industry/Entity Type

Marketing

Requirements
Must have
• Concept needs to primarily capture our microencapsulation business; however, it would be nice to touch on our agglomeration business as well.
Nice to have
• Some sort of 3-d sphere to depict our coating solutions; possibly a hand holding a sphere.

Something that capture the idea that we do particle modification.

```html
<!DOCTYPE html>
<html lang="en">
<head>
<meta charset="utf-8">
<title>Harbor Milling Industries – particle processing of food ingredients</title>
<link href="https://fonts.googleapis.com/css2?family=Pathway+Gothic+One&family=Questrial&display=swap" rel="stylesheet">
<style>
  :root {
    --field: #7f7ff6;
    --field-edge: #f2f2ff;
    --ink: #000000;
    --brand-cyan: #00bfe7;
  }
  * { margin: 0; padding: 0; box-sizing: border-box; }
  html, body { width: 1032px; height: 1200px; overflow: hidden; }
  .poster {
    position: relative;
    width: 1032px;
    height: 1200px;
    background: linear-gradient(to right,
      var(--field-edge) 0%,
      var(--field) 11%,
      var(--field) 89%,
      var(--field-edge) 100%);
    color: var(--ink);
    font-family: "Questrial", sans-serif;
  }
  .brand-dot {
    position: absolute;
    left: 250px;
    top: 60px;
    width: 190px;
    height: 190px;
    border-radius: 50%;
    background: var(--brand-cyan);
  }
  .brand-name {
    position: absolute;
    left: 470px;
    top: 285px;
    font-family: "Questrial", sans-serif;
    font-size: 52px;
    line-height: 1.1;
    color: var(--ink);
  }
  .tagline {
    position: absolute;
    left: 0;
    width: 1032px;
    top: 485px;
    text-align: center;
    font-family: "Pathway Gothic One", sans-serif;
    font-size: 62px;
    letter-spacing: 0.5px;
  }
  .overview {
    position: absolute;
    left: 152px;
    top: 598px;
    width: 840px;
    font-size: 33px;
    line-height: 45px;
  }
</style>
</head>
<body>
  <main class="poster">
    <div class="brand-dot" aria-hidden="true"></div>
    <p class="brand-name">Harbor Milling<br>Industries</p>

    <h1 class="tagline">particle processing of food ingredients.</h1>

    <p class="overview">
      1) we microencapsulate (apply a coating)<br>
      to particles for a few different reasons<br>
      (examples: taste/color masking,<br>
      controlled or timed release of<br>
      ingredient, nutrient stability,<br>
      extending shelve-life, among others).<br>
      &nbsp;2) we agglomerate particles (make<br>
      particles stick together to make them<br>
      go into solution better/faster)<br>
      Everything we do is customize to our<br>
      customers specifications. We use the<br>
      term "Solutions Engineering" quite a<br>
      &nbsp;bit in our marketing materials.
    </p>
  </main>
</body>
</html>
```